Business Card Design Project

I need a business card designed with these details on the front along with the logo attached on the front.

Address - 517/ 208 Wendlebury st Pellford
Website - www.brackwoodcarvers.com.au
Email - delmar@brackwoodcarvers.com.au
Fax - 1900 417 562
Mobile - 0471390618
Telephone - 1300627059
Licence number - 864207k

```html
<!DOCTYPE html>
<html lang="en">
<head>
<meta charset="utf-8">
<title>Brackwood Carvers – Business Card</title>
<link rel="stylesheet" href="https://fonts.googleapis.com/css2?family=PT+Sans:wght@400;700&display=swap">
<style>
  :root {
    --page: #ffffff;
    --card: #ffffff;
    --card-edge: #8a8a8a;
    --ink: #111111;
    --maroon: #6b2829;
    --maroon-text: #7a2e30;
    --band-text: #ffffff;
    --mark-fill: #cbb89a;
    --mark-edge: #a8916f;
    --brand-ink: #3a2a22;
  }
  * { margin: 0; padding: 0; box-sizing: border-box; }
  html, body {
    width: 1200px; height: 1067px; overflow: hidden;
    background: var(--page);
    font-family: "PT Sans", Arial, sans-serif;
  }
  .card {
    position: absolute; left: 99px; top: 227px;
    width: 1002px; height: 612px;
    background: var(--card);
    border: 1px solid var(--card-edge);
    border-bottom: none;
  }
  .brand {
    position: absolute; left: 503px; top: 35px;
    display: flex; align-items: center; gap: 20px;
  }
  .brand-square {
    width: 106px; height: 102px;
    background: var(--mark-fill);
    border: 2px solid var(--mark-edge);
  }
  .brand-name {
    font-size: 42px; line-height: 50px; font-weight: 400;
    color: var(--brand-ink); letter-spacing: 0.5px;
  }
  .person {
    position: absolute; left: 33px; top: 248px;
  }
  .person-name { font-size: 34px; line-height: 40px; color: var(--ink); }
  .person-role { font-size: 22px; line-height: 30px; color: var(--maroon-text); }
  .divider {
    position: absolute; left: 0; right: 0; top: 346px;
    height: 2px; background: var(--maroon); opacity: 0.75;
  }
  .contact-band {
    position: absolute; left: -1px; right: -1px; top: 366px; bottom: 0;
    background: var(--maroon); color: var(--band-text);
    padding: 36px 0 0 33px;
  }
  .address { font-size: 31px; font-weight: 700; line-height: 40px; margin-bottom: 6px; }
  .contact-row { display: flex; font-size: 23px; line-height: 34px; }
  .contact-label { width: 108px; font-weight: 700; }
  .contact-colon { width: 30px; font-weight: 700; }
  .contact-value b { font-weight: 700; }
</style>
</head>
<body>
  <section class="card">
    <div class="brand">
      <div class="brand-square"></div>
      <div class="brand-name">BRACKWOOD<br>CARVERS</div>
    </div>

    <div class="person">
      <div class="person-name">PERSON NAME</div>
      <div class="person-role">Designation</div>
    </div>

    <div class="divider"></div>

    <div class="contact-band">
      <div class="address">517/ 208 Wendlebury st Pellford</div>
      <div class="contact-row"><span class="contact-label">Mobile</span><span class="contact-colon">:</span><span class="contact-value">0471390618, <b>Licence No :</b> 864207k</span></div>
      <div class="contact-row"><span class="contact-label">Tel. No</span><span class="contact-colon">:</span><span class="contact-value">1300627059, <b>Fax :</b> 1900 417 562</span></div>
      <div class="contact-row"><span class="contact-label">Email</span><span class="contact-colon">:</span><span class="contact-value">delmar@brackwoodcarvers.com.au</span></div>
      <div class="contact-row"><span class="contact-label">Web</span><span class="contact-colon">:</span><span class="contact-value">www.brackwoodcarvers.com.au</span></div>
    </div>
  </section>
</body>
</html>
```